TOWNHAX3 Research Outcomes (e-Toolkit)

I would like you to design an electronic document that can be used to display the outcomes of the TOWNHAX3 Research that can easily be downloaded from a website. This document will help nurses, educators, students and their supervisors to be able to better understand the outcomes of the research and apply it to their own practice. It should be something they can print out (A4 size) and refer to easily. It should be quite graphical and represent male and female nurses working in different specialty areas (emergency, primary healthcare, aged care, etc.), across hospital to primary healthcare (community) contexts. It should be professional, clean and crisp in appearance. There are areas in yellow in the attached document that are yet to be determined. All images within the document can be amended to better reflect the design of the document and the intent of its contained content. An example of the type of document I'm looking for is attached as "standards.pdf". It should be approximately 15 pages in length.
Updates

The project does not have to use the TOWNHAX3 logo or its colours as a main design feature of the project.

Target Market(s)

Nurses, educators and students.

Industry/Entity Type

Education

Font styles to use
Sans Serif

Colors

Designer to choose colors to be used in the design.

Requirements
Must have
• Must have a diagram depicting the interrelatedness of all the individual metaspecialties. The contained diagrams can be modified to suit graphic design needs.
• Images of nursing professionals should appear Australian.
Nice to have
• I would like them to try and re-configure the diagrams as they are boring and I hate the colours. Images of collaboration amongst different healthcare team members would be nice.
Should not have
• Only images of female nurses or only images (if chosen) of nurses only working in a hospital.

```html
<!DOCTYPE html>
<html lang="en">
<head>
<meta charset="utf-8">
<title>TOWNHAX3 Toolkit – Licence and Application</title>
<link rel="stylesheet" href="https://fonts.googleapis.com/css2?family=Quicksand:wght@400;500;600;700&display=swap">
<style>
  :root {
    --backdrop: #e8e7e4;
    --paper: #fbfbfb;
    --ink: #4a4a4a;
    --ink-soft: #666666;
    --teal: #1faa98;
    --teal-link: #2bb3a3;
    --teal-pale: #a8ddd3;
    --edge-orange: #e8773e;
    --line: 17.8px;
  }
  * { box-sizing: border-box; margin: 0; padding: 0; }
  html, body {
    width: 1200px; height: 756px; overflow: hidden;
    background: var(--backdrop);
    font-family: "Quicksand", sans-serif;
  }
  .spread {
    position: absolute; left: 49px; top: 28px;
    width: 1102px; height: 700px;
    display: flex;
  }
  .page {
    position: relative; width: 551px; height: 700px;
    background: var(--paper);
    color: var(--ink);
    font-size: 11.4px; line-height: var(--line);
    font-weight: 500;
  }
  .page--left { border-left: 6px solid var(--edge-orange); }
  .page--right { border-right: 6px solid var(--edge-orange); }
  .page-header-art {
    position: absolute; top: 0; height: 165px;
  }
  .page--left .page-header-art {
    left: 0; width: 500px;
    background: linear-gradient(160deg, var(--teal-pale) 0%, rgba(168,221,211,0.55) 40%, rgba(168,221,211,0) 85%);
  }
  .page--right .page-header-art {
    left: 0; width: 490px;
    background: linear-gradient(165deg, var(--teal-pale) 0%, rgba(168,221,211,0.5) 35%, rgba(168,221,211,0) 80%);
  }
  .page-number {
    position: absolute; top: 676px; left: 32px;
    font-size: 8px; color: var(--ink-soft);
  }
  .licence {
    position: absolute; left: 94px; top: 171px; width: 370px;
    color: var(--ink-soft);
  }
  .licence h2, .citation-label {
    font-size: 11.4px; font-weight: 700; color: var(--ink-soft);
  }
  .licence p { margin-top: var(--line); }
  .link { color: var(--teal-link); }
  .citation { color: var(--teal-link); }
  .application {
    position: absolute; left: 31px; top: 68px; width: 450px;
  }
  .application h1 {
    font-size: 22px; font-weight: 700; color: var(--teal);
    letter-spacing: 0.3px; line-height: 26px;
    margin-bottom: 65px;
  }
  .audience { margin-bottom: var(--line); }
  .audience ul { list-style: none; padding-left: 60px; }
  .audience li { position: relative; }
  .audience li::before {
    content: "·"; position: absolute; left: -24px; color: var(--ink-soft);
  }
</style>
</head>
<body>
<main class="spread">
  <section class="page page--left">
    <div class="page-header-art" role="img" aria-label="Decorative pattern of scattered pale teal triangles"></div>
    <div class="licence">
      <h2>OpenShare licence statement</h2>
      <p>This document is licensed under a OpenShare Attribution-ShareAlike 4.0 International License<br>
        <span class="link">http://openshare-licences.org/by-sa/4.0/.</span></p>
      <p>The details of the relevant license conditions are available on the OpenShare website (accessible<br>
        using the links provided) as is the full legal code for the OpenShare Attribution-ShareAlike 4.0 International License<br>
        <span class="link">http://openshare-licences.org/by-sa/4.0/legalcode.</span></p>
      <p>You are free to copy, communicate and adapt the work, as long as you attribute the work as indicated by the suggested citation below.</p>
      <p><span class="citation-label">Suggested citation:</span><br>
        <span class="citation">Hartley A., Morrow G., Quill F., Dunne., Vance C.<br>
        TOWNHAX3 Clinical Specialty Learning And<br>Capability: A Toolkit. (2018).</span></p>
    </div>
    <span class="page-number">ii</span>
  </section>

  <section class="page page--right">
    <div class="page-header-art" role="img" aria-label="Decorative pattern of scattered pale teal triangles"></div>
    <div class="application">
      <h1>APPLICATION</h1>
      <div class="audience">
        <p>This toolkit will be used by university academic staff to:</p>
        <ul>
          <li>Develop clinical learning outcomes for nurse practitioner students' chosen specialty areas,</li>
          <li>Support the learning and teaching of nurse practitioner students,</li>
          <li>Inform nurse practitioner Master's degree course curricula,</li>
          <li>Understand the specialty clinical skills, knowledge and expertise needed by nurse practitioner students during periods of Integrated Professional Practice.</li>
        </ul>
      </div>
      <div class="audience">
        <p>This toolkit will be used by clinical mentoring staff and broader clinical teams involved in nurse practitioner student clinical education to:</p>
        <ul>
          <li>Develop clinical learning outcomes for nurse practitioner Support the clinical learning and teaching of nurse practitioner students,</li>
          <li>Understand the specialty clinical skills, knowledge and expertise needed by nurse practitioner students during periods of Integrated Professional Practice.</li>
        </ul>
      </div>
      <div class="audience">
        <p>This toolkit will be used by nurse practitioner students to:</p>
        <ul>
          <li>Identify the specialty clinical skills, knowledge and expertise needed to practice as a novice nurse practitioner once endorsed,</li>
          <li>Develop clinical learning outcomes for nurse practitioner students' chosen specialty areas during periods of Integrated Professional Practice.</li>
        </ul>
      </div>
      <div class="audience">
        <p>This toolkit will be used by endorsed nurse practitioners to:</p>
        <ul>
          <li>Identify specialty clinical skills, knowledge and expertise to guide expansion of clinical expertise,</li>
          <li>Inform professional development goals.</li>
        </ul>
      </div>
    </div>
    <span class="page-number">6</span>
  </section>
</main>
</body>
</html>
```